Letterhead for 3 attorney Workers' Comp law firm

We are a 3 attorney law office. We specialize in Workers' Compensation. Our office represents workers who are injured on the job, and the estates of workers who are killed one the job.
When we started our office, we created our own letterhead & have been using it for years. We've just recently hired the 3rd attorney, and were going to just add his name to the letterhead, but have decided we wanted to get a professionally designed letterhead and business cards at this point.
We want something that looks clean and professional. It must look good in black and white because we often make multiple copies of our documents. We're hoping for a design that resonates confidence, reliability and experience.
The design must include the firm name: Dorrance & Pike, PLLC. We would like the PLLC to be small compared to the Dorrance & Pike graphic. We also want to incorporate the attorney names: Ulric Dorrance, Janet Pike, and Lyle Hagberg. Our current letterhead has our contact info in the footer at the bottom of the page. We like that design, but are open to the idea of having it at the top. We'll leave that at the discretion of the designer. Our contact info is as follows: 472 S. Larchmont Avenue, Suite 315 Bellingham, WA 98117 Phone: 360-514-2967, Fax: 360-521-6079, and our website: www.dorrancepike-law.example
Target Market(s)
Clients, courts, other legal offices, doctors offices. These are the people who see our letterhead most frequently. It's not so much for marketing purposes, mainly so that we have a professional image when sending out documents.
Industry/Entity Type
Law Firm
Contact Information for Business Card
On the back of the business card: it can be designed, or be a template for filling in appointment reminder information (i.e. date, time, etc)
Colors
Designer to choose colors to be used in the design.
Requirements
Must have
- Must have our firm name at the top.
- Must include the attorney names.
- Must have all of our contact information (can be at top or bottom - whatever looks best with the design)
Nice to have
- A strong, confident design
Should not have
- We don't want the design to be playful, cartoony or busy.

```html
<!DOCTYPE html>
<html lang="en">
<head>
<meta charset="utf-8">
<title>Dorrance &amp; Pike, PLLC — Stationery</title>
<link rel="stylesheet" href="https://fonts.googleapis.com/css2?family=Arimo:wght@400&family=Didact+Gothic&family=Libre+Baskerville:wght@400&family=Raleway:wght@400&display=swap">
<style>
  :root {
    --navy: #2c4473;
    --blue: #2a7cc7;
    --ink: #6d6e71;
    --ink-soft: #8a8b8e;
    --rule: #9a9ba0;
    --band-grey: #7f8083;
    --paper: #ffffff;
    --backdrop: #d4d4d7;
  }
  * { margin: 0; padding: 0; box-sizing: border-box; }
  html, body { width: 1200px; height: 1200px; overflow: hidden; }
  body { background: var(--backdrop); position: relative; font-family: "Arimo", Arial, sans-serif; }

  .letterhead, .card { position: absolute; background: var(--paper); overflow: hidden; }
  .letterhead { left: 198px; top: 213px; width: 512px; height: 723px; }

  .contact { position: absolute; font-size: 8.3px; line-height: 13px; color: var(--ink); }
  .contact .label { color: var(--navy); }
  .letterhead .contact { left: 34px; top: 16px; }

  .brand { position: absolute; }
  .brand-square { position: absolute; border: 1px solid var(--navy); }
  .brand-divider { position: absolute; width: 1px; background: var(--rule); }
  .brand-name { position: absolute; font-family: "Libre Baskerville", Georgia, serif; font-weight: 400; color: var(--ink); white-space: nowrap; }
  .brand-suffix { position: absolute; font-family: "Libre Baskerville", Georgia, serif; font-weight: 400; color: var(--ink); text-align: center; display: flex; align-items: center; gap: 4px; }
  .brand-suffix::before, .brand-suffix::after { content: ""; flex: 1; height: 1px; background: var(--rule); }

  .letterhead .brand-square { left: 270px; top: 26px; width: 38px; height: 38px; }
  .letterhead .brand-divider { left: 322px; top: 18px; height: 52px; }
  .letterhead .brand-name { left: 331px; top: 28px; font-size: 17.5px; }
  .letterhead .brand-suffix { left: 331px; top: 55px; width: 186px; font-size: 9px; }

  .headline { position: absolute; left: 156px; top: 129px; font-family: "Raleway", sans-serif; font-size: 23px; color: var(--ink); letter-spacing: 0.5px; }
  .headline .accent { color: var(--blue); }
  .subhead { position: absolute; left: 162px; top: 170px; width: 200px; font-size: 8.2px; line-height: 10.5px; color: var(--ink); }

  .body-copy { position: absolute; left: 76px; top: 213px; width: 370px; font-family: "Didact Gothic", sans-serif; font-size: 10.6px; line-height: 14.6px; letter-spacing: 0.55px; color: var(--ink); }
  .body-copy p + p { margin-top: 14.6px; }

  .signature { position: absolute; left: 76px; top: 530px; width: 70px; height: 22px; background: linear-gradient(90deg, #e6e6e8, #dcdcdf); }

  .footer-band { position: absolute; left: 0; bottom: 0; width: 100%; height: 14px; }
  .footer-band svg { display: block; }
  .footer-address { position: absolute; left: 90px; bottom: 2px; font-size: 8px; color: #fff; }

  .card { left: 796px; width: 219px; height: 122px; }
  .card-front { top: 411px; }
  .card-back { top: 601px; }
  .card-front .brand-divider { left: 119px; top: 38px; height: 54px; background: var(--navy); }
  .card-front .contact { left: 128px; top: 39px; font-size: 6.3px; line-height: 10px; }
  .card-band { position: absolute; left: 0; bottom: 0; width: 100%; height: 10px; background: var(--navy); color: #fff; font-size: 6px; line-height: 10px; padding-left: 25px; }

  .card-back .brand-square { left: 22px; top: 44px; width: 32px; height: 32px; }
  .card-back .brand-divider { left: 69px; top: 38px; height: 46px; }
  .card-back .brand-name { left: 77px; top: 48px; font-size: 13.5px; }
  .card-back .brand-suffix { left: 77px; top: 69px; width: 126px; font-size: 7.5px; }
</style>
</head>
<body>

<section class="letterhead">
  <div class="contact">
    <div>Ulric Dorrance</div>
    <div>Janet Pike</div>
    <div>Lyle Hagberg</div>
    <div><span class="label">Phone:</span> 360-514-2967</div>
    <div><span class="label">Fax:</span> 360-521-6079</div>
    <div><span class="label">Web:</span> www.dorrancepike-law.example</div>
  </div>

  <div class="brand-square"></div>
  <div class="brand-divider"></div>
  <div class="brand-name">Dorrance &amp; Pike</div>
  <div class="brand-suffix">PLLC</div>

  <h1 class="headline">YOUR<span class="accent">HEADLINE</span></h1>
  <p class="subhead">Lorem ipsum dolor sit amet, consectetuer adipi-scing elit, sed diam</p>

  <div class="body-copy">
    <p>Lorem ipsum dolor sit amet, consectetuer adipiscing elit, sed diam nonummy nibh euismod tincidunt ut laoreet dolore magna aliquam erat volutpat. Ut wisi enim ad minim veniam, quis nostrud exerci tation ullamcorper suscipit lobortis nisl ut aliquip ex ea commodo consequat. Duis autem vel eum iriure dolor in hendrerit in vulputate velit esse molestie consequat, vel illum dolore eu feugiat nulla facilisis at vero eros et accumsan et iusto odio dignissim qui bladit praesent luptatum zzril delenit augue duis dolore te feugait nulla facilisi.</p>
    <p>Nam liber tempor cum soluta nobis eleifend option congue nihil imperdiet doming id quod mazim placerat facer possim assum. Typi non habent claritatem insitam; est usus legentis in iis qui facit eorum claritatem. Investigationes demonstraverunt lectores legere me lius quod ii legunt saepius. Claritas est etiam processus dynamicus, qui sequitur mutationem consuetudium lectorum.</p>
    <p>Mirum est notare quam littera gothica, quam nunc putamus parum claram, anteposuerit litterarum formas humanitatis per seacula quarta decima et quinta decima. Eodem modo typi, qui nunc nobis videntur parum clari, fiant sollemnes in futurum.</p>
  </div>

  <div class="signature" role="img" aria-label="Handwritten signature"></div>

  <div class="footer-band">
    <svg width="512" height="14" viewBox="0 0 512 14">
      <rect x="0" y="0" width="512" height="14" fill="var(--band-grey)"/>
      <polygon points="0,0 392,0 404,14 0,14" fill="var(--navy)"/>
    </svg>
    <div class="footer-address">472 S. Larchmont Avenue, Suite 315 Bellingham, WA 98117</div>
  </div>
</section>

<section class="card card-front">
  <div class="brand-divider"></div>
  <div class="contact">
    <div>Ulric Dorrance</div>
    <div>Janet Pike</div>
    <div>Lyle Hagberg</div>
    <div><span class="label">Phone:</span> 360-514-2967</div>
    <div><span class="label">Fax:</span> 360-521-6079</div>
    <div><span class="label">Web:</span> www.dorrancepike-law.example</div>
  </div>
  <div class="card-band">472 S. Larchmont Avenue, Suite 315 Bellingham, WA 98117</div>
</section>

<section class="card card-back">
  <div class="brand-square"></div>
  <div class="brand-divider"></div>
  <div class="brand-name">Dorrance &amp; Pike</div>
  <div class="brand-suffix">PLLC</div>
</section>

</body>
</html>
```